Wedding Startup Full Website Design

We've just completed our online platform and need to create a website that represents our brand and vision, and clearly communicates our features and value proposition to potential users. There are a minimum of 4 pages that need to be designed. One geared toward wedding professionals (venues/vendors/coordinators), another toward engaged couples, one showcasing features, and an 'About Us' page.

The designer will creative freedom to create a unique UI/UX as long as it represents our brand and is relevant to our target audience/market. The ideal candidate will be able to assume the mindset of someone working in the wedding industry and/or an engaged couple. Ability to create illustrations is a plus.

Copy will be provided as needed. We will reimburse for stock images (pending approval before purchasing), but sourcing the stock images will be the responsibility of the designer.

Our current website: https://www.wedloom.com
Updates

Still waiting for a design that stands out from the rest and aligns with the creative brief.

Target Market(s)

Wedding Professionals and Engaged Couples

Industry/Entity Type

Wedding

Number of Pages Required

4 page

Font styles to use
Sans Serif

Colors
ffffff
fbd4d5
f59195
33a6d7
cadf82
86cfc6

Requirements
Must have
• Common sense stuff like having a unified brand that accurately represents our platform, speaks to our target market, and clearly articulates our vision
Nice to have
• Illustrations
Should not have
• Overly cheesy or childish. We want to be professional but still embrace the wedding culture.

```html
<!DOCTYPE html>
<html lang="en">
<head>
<meta charset="utf-8">
<title>Wedloom — Demo Platform</title>
<link href="https://fonts.googleapis.com/css2?family=Raleway:wght@200;300;400;500&display=swap" rel="stylesheet">
<style>
  :root {
    --page: #ffffff;
    --ink: #1f1f1f;
    --nav-ink: #333333;
    --brand-blue: #5aaee0;
    --coral: #f47f82;
    --coral-light: #f79597;
    --rule: #bdbdbd;
    --footer-band: #f7f7f7;
    --divider: #e6e6e6;
  }
  * { margin: 0; padding: 0; box-sizing: border-box; }
  html, body {
    width: 1200px; height: 1200px; overflow: hidden;
    background: var(--page);
    font-family: "Raleway", sans-serif;
    color: var(--ink);
  }
  .canvas { position: relative; width: 1200px; height: 1200px; }

  .site {
    position: absolute; left: 24px; top: 302px;
    width: 1152px; height: 612px; overflow: hidden;
  }
  .hero-photo {
    position: absolute; inset: 0;
    background: linear-gradient(180deg,
      #ffffff 0%, #eef1f4 12%, #dde3e8 28%, #cbd5dc 44%,
      #9db5c0 56%, #a9bec8 64%, #dfe6ea 76%, #f3f5f7 100%);
  }

  .site-header {
    position: absolute; left: 0; top: 0; width: 100%; height: 66px;
  }
  .brand {
    position: absolute; left: 69px; top: 13px;
    font-size: 30px; font-weight: 400; color: var(--brand-blue);
    letter-spacing: 0.3px; white-space: nowrap;
  }
  .main-nav {
    position: absolute; top: 26px; left: 0; width: 100%;
    font-size: 12px; font-weight: 400; color: var(--nav-ink);
  }
  .main-nav a { position: absolute; color: inherit; text-decoration: none; white-space: nowrap; }
  .nav-search { position: absolute; left: 916px; top: 22px; width: 18px; height: 18px; }
  .btn-access {
    position: absolute; left: 966px; top: 13px; width: 127px; height: 36px;
    background: var(--coral); color: #fff;
    font-size: 13px; font-weight: 400; letter-spacing: 0.3px;
    display: flex; align-items: center; justify-content: center;
    border-radius: 2px;
  }

  .welcome-card {
    position: absolute; left: 30px; top: 187px; width: 657px; height: 425px;
    background: #fff; box-shadow: 0 2px 14px rgba(0,0,0,0.08);
  }
  .welcome-title {
    position: absolute; left: 39px; top: 40px;
    font-size: 58px; font-weight: 200; line-height: 68px; letter-spacing: -0.5px;
    color: var(--ink); white-space: nowrap;
  }
  .title-accent {
    position: absolute; left: 456px; top: 147px; width: 148px; height: 2px;
    background: var(--coral);
  }
  .welcome-lead {
    position: absolute; left: 39px; top: 189px;
    font-size: 23px; font-weight: 400; color: var(--ink); white-space: nowrap;
  }
  .email-field {
    position: absolute; left: 39px; top: 246px; width: 409px; height: 36px;
    border-bottom: 1px solid var(--rule);
  }
  .email-field span {
    position: absolute; left: 14px; top: 11px; font-size: 12px; color: #444;
  }
  .btn-next {
    position: absolute; left: 477px; top: 247px; width: 127px; height: 36px;
    background: var(--coral-light); color: #fff;
    font-size: 13px; letter-spacing: 0.3px;
    display: flex; align-items: center; justify-content: center;
    border-radius: 2px;
  }
  .social-band {
    position: absolute; left: 0; bottom: 0; width: 100%; height: 101px;
    background: var(--footer-band); border-top: 1px solid var(--divider);
  }
  .social-label {
    position: absolute; left: 39px; top: 34px;
    font-size: 23px; font-weight: 300; color: var(--ink);
  }
  .social-btn {
    position: absolute; top: 20px; width: 54px; height: 54px; border-radius: 50%;
    background: #fff; box-shadow: 0 3px 8px rgba(0,0,0,0.12);
    display: flex; align-items: center; justify-content: center;
    font-size: 12px; font-weight: 500; color: #555;
  }
</style>
</head>
<body>
<div class="canvas">
  <section class="site">
    <div class="hero-photo" role="img" aria-label="Photo of a wedding couple embracing on a snowy shore beside a misty grey-blue sea"></div>

    <header class="site-header">
      <div class="brand">Wedloom</div>
      <nav class="main-nav">
        <a style="left:609px">Home</a>
        <a style="left:670px">About us</a>
        <a style="left:745px">Features</a>
        <a style="left:822px">For couples</a>
      </nav>
      <svg class="nav-search" viewBox="0 0 18 18" fill="none" stroke="#333" stroke-width="1.3">
        <circle cx="10.5" cy="7.5" r="5.5"/>
        <line x1="6.6" y1="11.4" x2="2" y2="16"/>
      </svg>
      <div class="btn-access">ACCESS DEMO</div>
    </header>

    <div class="welcome-card">
      <h1 class="welcome-title">Welcome to Wedloom’s<br>demo platform.</h1>
      <div class="title-accent"></div>
      <p class="welcome-lead">Enter your email address to continue</p>
      <div class="email-field"><span>Email</span></div>
      <div class="btn-next">NEXT</div>

      <div class="social-band">
        <p class="social-label">Continue With:</p>
        <div class="social-btn" style="left:360px">Pals</div>
        <div class="social-btn" style="left:436px">Orbit</div>
        <div class="social-btn" style="left:512px">Chirp</div>
      </div>
    </div>
  </section>
</div>
</body>
</html>
```